Mavorika war genau die Richtige für mich. Sie hat zügig und professionell gearbeitet und ihr Entwurf hat genau meinen Geschmack getroffen. Die Kommunikation war sehr freundlich und klar.
Zielgruppe
Ich bin Systemische Coach und möchte eine Methode bewerben. Es geht dabei um Auflösung von Schocktraumata. Also Trauma nach Unfall, Gewalterfahrung, Katastrophe, Diagnose, Operation, traumatischer Geburt, etc.
Mein Flyer soll Menschen erreichen, die so etwas erlebt haben und bei denen das Ereignis immer noch getriggert wird. z.B. Polizist:innen, Rettungshelfer:innen, Ärzt:innen
Genaueres hier: www.ruhe-anker.de
Die Methode bietet schnelle Hilfe, arbeitet mit Visualisierung und Klopfen, und retraumatisiert nicht.
Aufgabenstellung
Design sollte sich an der Website orientieren. Texte können davon genommen werden.
Anbei noch ein Text, der in einem Veranstaltungsnewsletter erscheint.
Bildmaterial ebenfalls von Website (bitte dann anfragen, was gebraucht wird) oder sehr gerne auch anderes von bilder.quellmarkt.com
Format: Din lang, 4 Seiten, hoch oder quer ist egal

```html
<!DOCTYPE html>
<html lang="de">
<head>
<meta charset="utf-8">
<title>Flyer Silent Shore Technique</title>
<link rel="stylesheet" href="https://fonts.googleapis.com/css2?family=Roboto+Condensed:wght@400;700&family=Kalam:wght@300;400&display=swap">
<style>
:root{
  --bg:#e9e9ec;
  --paper:#f6f6f7;
  --paper-grey:#e6e6e8;
  --band:#8786bc;
  --band-dark:#5f60a6;
  --ink:#5a58b0;
  --text:#2c2c33;
  --box:#cbcae3;
  --seg1:#5f60a6;--seg2:#6f6eac;--seg3:#8786bc;--seg4:#c8c7e0;
}
*{margin:0;padding:0;box-sizing:border-box}
html,body{width:1200px;height:2625px;overflow:hidden;background:var(--bg)}
body{position:relative;font-family:"Roboto Condensed",Arial,sans-serif;color:var(--text)}
.spread{position:absolute;width:950px;display:flex;box-shadow:0 20px 40px rgba(0,0,0,.18)}
.outer{left:110px;top:110px;height:1060px}
.inner{left:120px;top:1380px;height:1050px}
.page{position:relative;width:475px;height:100%;overflow:hidden;background:var(--paper)}
.abs{position:absolute}
.script{font-family:"Kalam",cursive;font-weight:300}
.center{text-align:center}
.ink{color:var(--ink)}
.band{background:var(--band)}
.footer{position:absolute;left:0;bottom:0;width:100%;height:60px;background:var(--band-dark);color:#fff;font-size:24px;display:flex;align-items:center;justify-content:center}
.photo{position:absolute;background:linear-gradient(120deg,#d9c3a4 0%,#eae4dc 40%,#b9a08a 75%,#efe9e2 100%)}
.intro{left:40px;right:40px;top:70px;font-size:22px;line-height:1.2}
.intro .script{font-size:34px;margin:30px 0}
.contact{left:65px;top:500px;width:343px;height:465px;background:var(--box);text-align:center;font-size:20px;line-height:1.3;padding-top:38px}
.contact h3{font-size:22px;text-decoration:underline;color:var(--ink);margin-bottom:22px}
.contact .name{color:var(--ink);font-size:22px;margin-bottom:6px}
.contact ul{list-style:none;text-align:left;display:inline-block;margin:26px 0 36px}
.contact li{display:flex;align-items:center;gap:10px}
.contact svg{width:20px;height:20px;fill:var(--ink)}
.brand{left:0;right:0;top:240px;font-size:36px;color:var(--ink)}
.brand-mark{left:197px;top:80px;width:80px;height:80px;border-radius:50%;background:var(--box)}
.copy{left:55px;right:40px;font-size:16px;line-height:1.27;text-align:justify;hyphens:auto;-webkit-hyphens:auto;letter-spacing:-.1px}
.copy h4{font-size:17px;color:var(--ink);margin-bottom:12px}
.copy p{margin-bottom:11px}
.copy ul{list-style:none;text-align:left}
.copy li{position:relative;padding-left:13px;margin-bottom:8px}
.copy li::before{content:"•";position:absolute;left:0;color:var(--ink)}
.segs{position:absolute;left:0;bottom:0;width:100%;height:65px;display:flex}
.segs span{flex:1}
</style>
</head>
<body>

<section class="spread outer">
  <div class="page">
    <div class="abs intro center ink">
      <p>Sie müssen nicht mit schlimmen Erinnerungen leben und diese immer wieder durchleiden.</p>
      <p class="script">Es gibt eine Lösung!</p>
      <p>In einem vertraulichen Gespräch klären wir die Möglichkeiten.</p>
    </div>
    <div class="abs band" style="left:0;top:335px;width:100%;height:220px"></div>
    <p class="abs script center" style="left:0;right:0;top:360px;font-size:46px;line-height:1.1;color:#fff">Geben Sie sich<br>eine Chance!</p>
    <div class="abs contact">
      <h3>Kontakt:</h3>
      <p class="name">Lioba Venhart Sorelius</p>
      <p>Am Lindenhang 14<br>79288 Gerstau</p>
      <ul>
        <li><svg viewBox="0 0 24 24"><path d="M6.6 10.8a15 15 0 0 0 6.6 6.6l2.2-2.2a1 1 0 0 1 1-.25 11.4 11.4 0 0 0 3.6.57 1 1 0 0 1 1 1V20a1 1 0 0 1-1 1A17 17 0 0 1 3 4a1 1 0 0 1 1-1h3.5a1 1 0 0 1 1 1c0 1.25.2 2.45.57 3.6a1 1 0 0 1-.25 1z"/></svg>+49 (0)170 55 20 418</li>
        <li><svg viewBox="0 0 24 24"><path d="M2 5h20v14H2zm2 2v.5l8 5 8-5V7l-8 5z"/></svg>info@ruhe-anker.de</li>
        <li><svg viewBox="0 0 24 24"><circle cx="12" cy="12" r="9" fill="none" stroke="#5a58b0" stroke-width="1.6"/><path d="M3 12h18M12 3c-4 4.5-4 13.5 0 18M12 3c4 4.5 4 13.5 0 18" fill="none" stroke="#5a58b0" stroke-width="1.4"/></svg>www.ruhe-anker.de</li>
      </ul>
      <h3>Praxis:</h3>
      <p class="name">Praxis am Mühlbach</p>
      <p>Kornblumenweg 9<br>79104 Talbrunn</p>
    </div>
    <div class="footer">www.ruhe-anker.de</div>
  </div>
  <div class="page" style="background:var(--paper-grey)">
    <div class="abs brand-mark"></div>
    <p class="abs brand center">Silent Shore Technique</p>
    <div class="abs band center" style="left:0;top:335px;width:100%;height:220px;color:#fff;padding-top:28px">
      <p style="font-size:29px;line-height:1.2">Sie können Ihr<br>Schocktrauma auflösen!</p>
      <p style="font-size:21px;line-height:1.25;margin-top:18px">Befreien Sie sich von den Nachwirkungen<br>der Erfahrung und erleben Sie ein<br>unbeschwerteres, freieres Sein.</p>
    </div>
    <div class="photo" role="img" aria-label="Foto: Therapeutin im Gespräch mit einer Klientin in einem hellen Praxisraum" style="left:0;top:555px;width:100%;height:445px"></div>
    <div class="footer">www.ruhe-anker.de</div>
  </div>
</section>

<section class="spread inner">
  <div class="page" style="background:#ececee">
    <div class="abs band" style="left:0;top:0;width:100%;height:220px"></div>
    <div class="photo" role="img" aria-label="Foto: Therapeutin hört einer Klientin aufmerksam zu" style="left:25px;top:25px;width:440px;height:240px"></div>
    <div class="abs copy" style="top:300px">
      <h4>Hier eine Überschrift?</h4>
      <p class="ink">Sie haben Schlimmes erlebt und es sitzt Ihnen noch in den Knochen, hängt Ihnen nach, holt Sie ein, triggert Sie…? Sie erleben Albträume, Flashbacks, fühlen sich blockiert, verletzt, gebremst, beschämt, schuldig, überschattet, wie im Nebel, zerbrochen…?</p>
      <p>Egal, wie „groß“ oder „klein“ die Verletzung (griechisch: Trauma) war, lassen Sie nicht zu, dass sie Ihr Leben bestimmt, Sie beeinträchtigt, Sie davon abhält, Dinge zu tun, die Sie gerne tun würden.</p>
      <p>Sie brauchen nicht darauf zu warten, dass „die Zeit alle Wunden heilt“… Sie können jetzt sofort etwas tun, um die Verbindung zwischen dem Ereignis und den Mustern zu entkoppeln, die automatisch im Gehirn und Körper gestartet werden, sobald Sie etwas daran erinnert, es also einen Auslöser oder Trigger gibt.</p>
      <p>Dies gelingt mit der Anwendung der Silent Shore Technique – einer Methode, die durch eine Kombination aus Klopf-Akupressur und auditiv-visuellen-motorischen Reizen neuronale Veränderungen im Gehirn bewirkt. Neuronale Muster, die durch das Trauma entstanden sind, werden gelöst und neu konditioniert.</p>
      <p class="ink" style="text-align:left">Das Geschehene wird zu einer normalen Erinnerung und löst keine Symptome mehr aus.</p>
    </div>
    <div class="segs"><span style="background:var(--seg1)"></span><span style="background:var(--seg2)"></span></div>
  </div>
  <div class="page">
    <div class="abs band" style="left:0;top:0;width:100%;height:220px"></div>
    <div class="abs" style="left:230px;top:0;width:245px;height:290px;background:var(--seg4)"></div>
    <div class="photo" role="img" aria-label="Foto: Therapeutin zeigt einer Klientin die Klopfpunkte an der Stirn" style="left:20px;top:25px;width:410px;height:245px"></div>
    <div class="abs copy" style="top:292px;left:40px;right:30px;text-align:left">
      <h4>Was macht SST so einzigartig?</h4>
      <ul>
        <li>Der SST-Prozess ist sehr sanft. Eine Sitzung mit SST ist in der Regel wenig belastend, wodurch das Retraumatisierungsrisiko sehr gering ist.</li>
        <li>Die Technik ist so konzipiert, dass schon früh im Prozess im sicheren Abstand vom Fühlen gearbeitet wird. Hierdurch braucht es wenig stabilisierende Vorarbeit.</li>
        <li>SST ist ein relativ schneller Prozess. Die meisten Schocktraumata lassen sich im Rahmen einer Sitzung lösen.</li>
        <li>Die erleichternde Wirkung ist sofort spürbar.</li>
        <li>Basierend auf jahrelangen Erfahrungen von Mirella Osgood und vieler SST-Anwender/innen weltweit, wirkt eine genau nach dem Protokoll durchgeführte Sitzung nachhaltig und braucht in der Regel keine Folgesitzungen oder sonstige Nachbearbeitung.</li>
        <li>SST eignet sich sowohl für Erwachsene als auch für Kinder aller kultureller und religiöser Hintergründe.</li>
        <li>Die Technik kann auf alle belastenden Erinnerungen, die einen Schock- oder Schreckmoment enthalten, angewandt werden.</li>
        <li>Dabei ist es unerheblich, wie lange das Erlebte zurückliegt. Es muss nur eine bewusste Erinnerung in Form von Gesehenem oder Gehörtem vorhanden sein.</li>
      </ul>
    </div>
    <div class="segs"><span style="background:var(--seg3)"></span><span style="background:var(--seg4)"></span></div>
  </div>
</section>

</body>
</html>
```